Amber Hollow Productions

I need a business card design for a new freelance film production company using or incorporating the logo:
I want the card to be creative, minimal, yet professional. Feel free to use a variety of different shapes and sizes/ textures for the card.

Industry/Entity Type

Film Production

```html
<!DOCTYPE html>
<html lang="en">
<head>
<meta charset="utf-8">
<title>Amber Hollow Productions – Business Card</title>
<link rel="stylesheet" href="https://fonts.googleapis.com/css2?family=Lato:wght@300;400;700&display=swap">
<style>
  :root {
    --backdrop: #35302d;
    --brand-blue: #3d5fd8;
    --brand-blue-deep: #1f3f9e;
    --band-blue: #2f4fc0;
    --card-white: #ffffff;
    --text-grey: #555a60;
    --text-soft: #6b7076;
  }
  * { box-sizing: border-box; margin: 0; padding: 0; }
  html, body {
    width: 1200px; height: 716px; overflow: hidden;
    background: var(--backdrop);
    font-family: "Lato", Arial, sans-serif;
  }
  .canvas {
    position: relative; width: 1200px; height: 716px;
    display: flex; align-items: center; justify-content: center; gap: 40px;
  }
  .card {
    position: relative; width: 520px; height: 300px;
    box-shadow: 0 10px 30px rgba(0,0,0,.45);
    overflow: hidden;
  }

  /* Front */
  .card-front {
    background: var(--brand-blue);
    display: flex; align-items: center; justify-content: center;
  }
  .front-wordmark {
    color: var(--brand-blue-deep);
    font-weight: 400;
    font-size: 34px;
    letter-spacing: 2px;
    text-align: center;
    line-height: 1.25;
    text-transform: uppercase;
  }

  /* Back */
  .card-back { background: var(--card-white); }
  .edge-band {
    position: absolute; left: 0; right: 0; height: 14px;
    background: var(--band-blue);
  }
  .edge-band.top { top: 0; }
  .edge-band.bottom { bottom: 0; }

  .back-wordmark {
    position: absolute; left: 26px; top: 34px;
    color: var(--brand-blue-deep);
    font-weight: 400;
    font-size: 34px;
    letter-spacing: .5px;
    text-transform: uppercase;
    line-height: 1.05;
  }
  .back-wordmark span { display: block; }

  .person {
    position: absolute; left: 26px; top: 126px;
    color: var(--text-grey);
    display: flex; align-items: baseline; gap: 6px;
  }
  .person-name { font-size: 22px; font-weight: 400; }
  .person-role { font-size: 12px; text-transform: uppercase; letter-spacing: .3px; }

  .contact-list {
    position: absolute; left: 26px; top: 170px;
    list-style: none; color: var(--text-soft); font-size: 12.5px;
  }
  .contact-list li { display: flex; align-items: center; gap: 8px; height: 18px; }
  .contact-list svg { width: 11px; height: 11px; flex: none; }

  .location {
    position: absolute; right: 30px; bottom: 40px;
    color: var(--text-soft); font-size: 12.5px; line-height: 18px;
    display: flex; gap: 8px;
  }
  .location-icons { display: flex; flex-direction: column; gap: 7px; padding-top: 3px; }
  .location-icons svg { width: 11px; height: 11px; }
  .website { font-weight: 700; color: var(--text-grey); }
  .website .domain { color: var(--brand-blue-deep); }
</style>
</head>
<body>
<main class="canvas">

  <section class="card card-front" aria-label="Card front">
    <p class="front-wordmark">Amber Hollow<br>Productions</p>
  </section>

  <section class="card card-back" aria-label="Card back">
    <div class="edge-band top"></div>

    <p class="back-wordmark">
      <span>Amber Hollow</span>
      <span>Productions</span>
    </p>

    <p class="person">
      <span class="person-name">Nadia Fairbrook</span>
      <span class="person-role">| Operation Manager</span>
    </p>

    <ul class="contact-list">
      <li>
        <svg viewBox="0 0 12 12" aria-hidden="true"><path d="M3 1l2 2.5-1.2 1.2a6 6 0 0 0 3.5 3.5L8.5 7 11 9l-1.5 2C5 11 1 7 1 2.5z" fill="none" stroke="#6b7076" stroke-width="1"/></svg>
        <span>+1 555 204 7731</span>
      </li>
      <li>
        <svg viewBox="0 0 12 12" aria-hidden="true"><rect x="3" y="1" width="6" height="10" rx="1" fill="none" stroke="#6b7076"/><line x1="5" y1="9.3" x2="7" y2="9.3" stroke="#6b7076"/></svg>
        <span>+61 400 555 019</span>
      </li>
      <li>
        <svg viewBox="0 0 12 12" aria-hidden="true"><rect x="1" y="3" width="10" height="7" fill="none" stroke="#6b7076"/><path d="M1 3l5 4 5-4" fill="none" stroke="#6b7076"/></svg>
        <span>name@amberhollow.me</span>
      </li>
    </ul>

    <div class="location">
      <div class="location-icons">
        <svg viewBox="0 0 12 12" aria-hidden="true"><circle cx="6" cy="6" r="5" fill="none" stroke="#6b7076"/><path d="M1 6h10M6 1c2 2 2 8 0 10M6 1c-2 2-2 8 0 10" fill="none" stroke="#6b7076" stroke-width=".8"/></svg>
        <svg viewBox="0 0 12 12" aria-hidden="true"><path d="M6 11S2 6.8 2 4.5a4 4 0 0 1 8 0C10 6.8 6 11 6 11z" fill="none" stroke="#6b7076"/><circle cx="6" cy="4.5" r="1.4" fill="#6b7076"/></svg>
      </div>
      <div class="location-text">
        <div class="website">www.<span class="domain">amberhollow</span>.com</div>
        <div>Rue des Tilleuls - Mont Clair</div>
        <div>BP 218 - City, Country</div>
      </div>
    </div>

    <div class="edge-band bottom"></div>
  </section>

</main>
</body>
</html>
```